Guide to Internet of Things Connectivity in Social Housing

THE SIZE of the booklet is A4.
We are producing a guide to the different types of internet of things (IoT) connectivity technology in the context of UK social housing.
The guide simply explains these technologies and provides examples of where they might be relevant in social housing.
The guide need a cover and feature a different technology on each page(wifi, z-wave, Bluetooth etc). It would be great to use some graphics to bring the pages to life and communicate a sense of 'networked connectivity' if it is possible to use logos for some of these technologies without copyright issues this could be good.
Ideally the guide will fit with our current organisation branding of black and gold/yellow.
Our website is www.tallowquay.io
FOR THE INITIAL ENTRIES:
I am happy for you to do a sample of the cover/back and some internal pages but no need to do all the pages at this stage.
Social Housing sector Professionals
Internet

```html
<!DOCTYPE html>
<html lang="en">
<head>
<meta charset="utf-8">
<title>IoT Connectivity in Social Housing – Guide Spreads</title>
<link href="https://fonts.googleapis.com/css2?family=Oswald:wght@500;700&family=Open+Sans:wght@400;600;700;800&display=swap" rel="stylesheet">
<style>
:root{
  --gold:#f39200;
  --gold-soft:#f7b24a;
  --ink:#141414;
  --paper:#ffffff;
  --canvas:#ececec;
  --illus-a:#f4f4f4;
  --illus-b:#dcdcdc;
}
*{box-sizing:border-box;margin:0;padding:0}
html,body{width:1200px;height:2608px;overflow:hidden;background:var(--canvas)}
body{font-family:"Open Sans",Arial,sans-serif;color:var(--ink);position:relative}
.spread{position:absolute;left:0;width:1200px;display:flex;box-shadow:0 4px 14px rgba(0,0,0,.18)}
.spread-intro{top:0;height:860px}
.spread-wan{top:880px;height:850px}
.spread-line{top:1750px;height:858px}
.page{position:relative;width:600px;height:100%;background:var(--paper);overflow:hidden;padding:40px 44px}
.page-dark{background:var(--ink);color:#fff}
.display{font-family:"Oswald",Impact,sans-serif;font-weight:700;text-transform:uppercase;line-height:1}
.p{font-size:10.5px;line-height:1.6;margin-bottom:12px;color:#333}
.page-dark .p{color:#ddd}
.lead{font-family:"Oswald",sans-serif;font-weight:700;font-size:18px;line-height:1.25;text-transform:uppercase;margin-bottom:16px}
/* intro */
.intro-band{position:absolute;left:0;top:0;width:600px;height:78px;background:var(--gold);padding:14px 40px}
.intro-band h1{font-size:48px;color:#fff}
.page-introduction{padding-top:120px}
.quote{font-size:11px;font-weight:700;color:var(--gold);line-height:1.5;margin-bottom:12px}
.quote small{display:block;font-size:9px;color:var(--ink);font-weight:800;letter-spacing:.04em;margin-top:4px}
.types-title{font-size:50px;color:#fff;margin-top:10px;margin-bottom:40px}
.types-title .gold{color:var(--gold)}
.types-sub{font-size:20px;color:var(--gold);margin-bottom:24px}
.types-cats{font-size:17px;color:var(--gold-soft);line-height:1.35;margin-bottom:22px}
.types-cats b{color:#fff}
.site{position:absolute;bottom:30px;right:44px;font-size:10px;color:var(--gold);font-weight:600}
/* corner marks */
.corner{position:absolute;width:0;height:0}
.corner-tl{left:0;top:0;border-top:70px solid var(--ink);border-right:70px solid transparent}
.corner-br{right:0;bottom:0;border-bottom:70px solid var(--ink);border-left:70px solid transparent}
.section-title{font-size:38px;margin:30px 0 24px}
.definition{font-size:14px;line-height:1.45;margin-bottom:16px}
.definition b{color:var(--gold)}
.illustration{position:absolute;background:radial-gradient(circle at 50% 45%,var(--illus-a),var(--illus-b));border-radius:4px}
.tag{display:inline-block;background:var(--gold);color:#fff;font-family:"Oswald",sans-serif;font-weight:700;font-size:22px;text-transform:uppercase;padding:6px 12px;line-height:1.15}
.tag-stack{max-width:300px}
.box{position:absolute;padding:12px 14px;font-size:10px;line-height:1.55}
.box h3{font-family:"Oswald",sans-serif;font-size:16px;margin-bottom:6px}
.box-pros{background:var(--gold);color:#fff}
.box-cons{background:var(--ink);color:#fff}
.box-cons h3{color:var(--gold)}
.box-soft{background:var(--gold-soft);color:var(--ink)}
.abs{position:absolute}
.strong-note{font-size:11px;font-weight:700;line-height:1.55}
</style>
</head>
<body>

<section class="spread spread-intro">
  <article class="page page-introduction">
    <div class="intro-band"><h1 class="display">Introduction</h1></div>
    <p class="lead">The Internet of Things (IoT) offers housing providers the opportunity to radically transform how they deliver their services.</p>
    <p class="p">One of the biggest opportunities exists where connected IoT technology can be leveraged to offer residents smarter ways to interact with their homes and to give housing providers a wider range of asset management benefits in social housing.</p>
    <p class="quote">For us in tech-led housing this is the potential that connected services now offer to residents and landlords alike.<small>SMART TECHNOLOGY, Tallowquay Housing Network</small></p>
    <p class="p">In order to realise this potential, these devices need to talk to each other and talk back to the internet. As it stands this is not yet straightforward. One of the areas where there is most diversity and confusion is in the underlying connectivity that enables the IoT to work.</p>
    <p class="p">In this paper we look at everything from broadband to bluetooth, to explain what all of these technologies are and what they mean for the solutions you might buy. While we will not make specific recommendations, our simplified overview will help you understand the potential pros and cons of adopting certain technologies as part of your IoT strategy.</p>
  </article>
  <article class="page page-dark page-types">
    <h2 class="display types-title">Understanding<br>connection <span class="gold">types</span></h2>
    <p class="display types-sub">In the IoT, a wide range of sensing and devices are connected to the internet.</p>
    <p class="types-cats">There are various technologies that provide that connection. These can be grouped into two categories: <b>wide area connections</b> and <b>local area connections</b>.</p>
    <p class="p">It is possible to run an IoT deployment by linking all of the sensors via a local area connection, and using a single wide area connection to report back to the internet. A sensor in isolated areas or where a single device located it can make sense to give that individual device a wide area connection.</p>
    <span class="site">www.tallowquay.io</span>
  </article>
</section>

<section class="spread spread-wan">
  <article class="page page-wan">
    <span class="corner corner-tl"></span>
    <h2 class="display section-title" style="margin-top:60px">Wide area connections</h2>
    <p class="definition">A <b>wide area connection (WAN)</b> is a network that transmits data over long distances. A mobile phone network is a good example of a WAN.</p>
    <p class="p">All of the technologies in this section are network data over distances of several miles or more. Typically this would be used to exchange data with the internet directly.</p>
    <p class="p">While some of these WAN technologies are widespread, many are new and have not yet reached critical mass. Of the ones that are best known, many are typically owned and managed by networks, making their use for IoT problematic.</p>
    <p class="p">This section covers some of the WAN technologies you could use in an IoT implementation.</p>
    <div class="illustration" role="img" aria-label="Illustration of transmission masts linked across a networked landscape of homes" style="left:30px;top:430px;width:540px;height:380px"></div>
  </article>
  <article class="page page-broadband">
    <span class="corner corner-br"></span>
    <span class="tag tag-stack">Resident broadband connection</span>
    <p class="definition" style="width:300px;margin-top:18px"><b>A broadband internet connection</b> consists of a copper or fibre optic connection from a property to the wider internet.</p>
    <p class="p" style="width:300px">A router or modem sits inside the property and controls the flow of data. There are different types of broadband — cable, ADSL, fibre and more. Each individual's options will vary depending on speed requirements and local availability.</p>
    <div class="box box-pros" style="left:370px;top:100px;width:190px;height:180px">
      <h3>Pros</h3>Private broadband can offer good speed and plenty of data for IoT, provided the resident is happy to connect devices to it and to keep the connection active. Where used alongside local networks, it can be a simple and low cost route.
    </div>
    <div class="box box-cons" style="left:370px;top:290px;width:190px;height:130px">
      <h3>Cons</h3>All your data is dependent on residents keeping their broadband in place. Devices can stop reporting when a resident changes provider, moves out or cancels.
    </div>
    <div class="illustration" role="img" aria-label="Illustration of a home router linked by cable to a street cabinet" style="left:44px;top:440px;width:512px;height:190px"></div>
    <p class="p abs" style="left:44px;top:648px;width:512px">Additionally, private broadband connections may not be available for IoT data transmission. The tenant may prefer that their connection is not available, or may have concerns about security and capacity. In some cases, it might be necessary to offer an incentive to the tenant in the form of broadband for keeping the connection active.</p>
    <p class="p abs" style="left:44px;top:730px;width:440px">A domestic connection is also unlikely to be under the control of the housing provider, unless it is owned or managed centrally. The connection could therefore be terminated, switched off or restricted without warning, making it an impractical option for on-going data transmission as is required for IoT.</p>
  </article>
</section>

<section class="spread spread-line">
  <article class="page page-lease">
    <h2 class="display section-title" style="margin-top:20px">Lease line</h2>
    <p class="definition" style="width:260px">Like a broadband connection, a <b>lease line</b> provides a physical internet connection to a building.</p>
    <p class="p" style="width:260px">A lease line will usually be a fibre connection with the option of high speed and low contention. These types of connections are typically used by businesses to connect their offices to the internet. Lease lines in housing are likely to be installed where the housing provider wants to provide a WiFi service to residents or an alternative to each resident purchasing their own broadband connection.</p>
    <div class="illustration" role="img" aria-label="Illustration of a fibre line running from a building to the internet" style="left:320px;top:110px;width:250px;height:400px"></div>
    <div class="box box-pros" style="left:44px;top:560px;width:250px;height:130px">
      <h3>Pros</h3>A lease line offers a fast, reliable connection which the housing provider owns and manages, giving full control over the data it carries.
    </div>
    <div class="box box-soft" style="left:44px;top:700px;width:250px;height:120px">
      <h3>Cons</h3>Lease lines are expensive and can take time to install. They are only cost effective where a site has enough devices or residents to share it.
    </div>
  </article>
  <article class="page page-cellular">
    <span class="tag">Cellular data network</span>
    <p class="definition" style="margin-top:18px;width:300px">All mobile phones and smartphones connect to a <b>cellular data network</b>. In the UK, we use the GSM standard.</p>
    <p class="p" style="width:300px">Data can be sent at various speeds, from 2G to 4G. The new 5G standard is due to be launched soon and will bring greater capacity.</p>
    <div class="illustration" role="img" aria-label="Illustration of a phone mast sending signals to homes and devices" style="left:360px;top:40px;width:200px;height:330px"></div>
    <div class="box box-pros" style="left:44px;top:400px;width:250px;height:220px">
      <h3>Pros</h3>Cellular networks are mature, widely available and well understood. A SIM-enabled device can be installed quickly anywhere there is a signal with no need for a resident's broadband. Modern low-power standards such as LTE-M extend battery life for simple sensors.
    </div>
    <div class="box box-soft" style="left:306px;top:400px;width:250px;height:220px">
      <h3>Cons</h3>Most cell operators require a monthly contract for each SIM, so costs rise with the number of devices. Coverage inside buildings and basements can be patchy, and older 2G and 3G networks are being switched off.
    </div>
    <p class="strong-note abs" style="left:44px;top:660px;width:512px">While industry estimates state that more than 90 per cent of the country has 4G coverage, some properties are located in areas only covered by older 2G, which offers one-tenth of the connection speed of 4G. Additionally, transmitting large amounts of data over 4G networks may be expensive.</p>
  </article>
</section>

</body>
</html>
```